DRIFTWATER a novel

He loves her, she loves him, and they work in a bar in Covent Garden. He is American; she is British. Brexit has happened and they don't care. His wife has called from America (ex-wife) and they don't care. They don't care about much because they are in their bar, and their bar is their haven. Sometimes it's Pelican Noir in there; sometimes it's the blues. They don't care. They are just a bit toooo cool, calm and collected. Let's send some wind up their sails.

Driftwater is the first in a three-part story about a man and a woman who love each other because life is simple. Music is important in the series, and music of the 70s, 80s and 90s. The covers have to capture their cool, easy way, and yet say "this is a love story". The books brings them their romance.

Author is Marnie Fenwick.

Image ideas: a Covent Garden setting for literal. A mermaid for symbolic. A music note for metaphorical. A lily for beauty.

```html
<!DOCTYPE html>
<html lang="en">
<head>
<meta charset="utf-8">
<title>Driftwater — a novel by Marnie Fenwick</title>
<link rel="stylesheet" href="https://fonts.googleapis.com/css2?family=Damion&family=Cormorant+Garamond:ital,wght@0,500;1,500&display=swap">
<style>
  :root {
    --page: #ffffff;
    --night: #14081f;
    --plum: #3a1250;
    --neon: #a21fae;
    --magenta: #d23ab8;
    --teal: #1f6c72;
    --deep-teal: #0d2a2e;
    --ink-white: #ffffff;
    --lily: #f29ac4;
  }
  html, body {
    margin: 0;
    width: 1200px;
    height: 1200px;
    overflow: hidden;
    background: var(--page);
  }
  .cover {
    position: absolute;
    left: 226px;
    top: 48px;
    width: 730px;
    height: 1095px;
    overflow: hidden;
    background: var(--night);
  }
  .bar-scene {
    position: absolute;
    inset: 0;
    background:
      radial-gradient(ellipse 70% 30% at 55% 38%, rgba(210,58,184,0.55), transparent 70%),
      linear-gradient(180deg, var(--night) 0%, var(--plum) 22%, var(--neon) 45%, var(--plum) 62%, var(--teal) 76%, var(--deep-teal) 90%, #050c0e 100%);
  }
  .music-notes {
    position: absolute;
    left: 0;
    top: 30px;
    width: 730px;
    height: 130px;
    background: linear-gradient(180deg, transparent, rgba(140,90,170,0.22) 50%, transparent);
  }
  .mermaid {
    position: absolute;
    left: 175px;
    top: 140px;
    width: 170px;
    height: 220px;
    background: rgba(255,255,255,0.85);
    border-radius: 50% 50% 40% 40%;
    filter: blur(1px);
  }
  .lily {
    position: absolute;
    left: 596px;
    top: 392px;
    width: 80px;
    height: 80px;
    background: var(--lily);
    border-radius: 50%;
  }
  .title {
    position: absolute;
    left: 40px;
    top: 345px;
    margin: 0;
    white-space: nowrap;
    font-family: "Damion", cursive;
    font-weight: 400;
    font-size: 138px;
    line-height: 1;
    color: var(--ink-white);
    text-shadow: 0 0 18px var(--magenta), 0 0 6px rgba(255,255,255,0.6);
  }
  .subtitle {
    position: absolute;
    left: 0;
    width: 100%;
    top: 532px;
    margin: 0;
    text-align: center;
    font-family: "Cormorant Garamond", serif;
    font-weight: 500;
    font-size: 56px;
    letter-spacing: 1px;
    color: var(--ink-white);
  }
  .byline {
    position: absolute;
    left: 0;
    width: 100%;
    top: 878px;
    margin: 0;
    text-align: center;
    color: var(--ink-white);
    font-family: "Cormorant Garamond", serif;
    font-weight: 500;
  }
  .byline-by {
    display: block;
    font-style: italic;
    font-size: 54px;
    line-height: 1;
  }
  .byline-author {
    display: block;
    margin-top: 16px;
    font-size: 56px;
    letter-spacing: 2px;
    line-height: 1;
  }
</style>
</head>
<body>
  <main class="cover">
    <div class="bar-scene" role="img" aria-label="Photograph of a neon-lit bar interior with bottle racks, signs and stools in purple and teal light"></div>
    <div class="music-notes" role="img" aria-label="Faint musical staff with notes drifting across the top"></div>
    <div class="mermaid" role="img" aria-label="White silhouette of a leaping mermaid"></div>
    <h1 class="title">Driftwater</h1>
    <div class="lily" role="img" aria-label="Pink lily flower"></div>
    <p class="subtitle">A NOVEL</p>
    <p class="byline">
      <span class="byline-by">by:</span>
      <span class="byline-author">MARNIE FENWICK</span>
    </p>
  </main>
</body>
</html>
```